Workplace Safety Consultancy Business needs business card design

We need a business card for a new business providing workplace health and safety consulting called 'Worksure Path'. We will be providing small to medium sized businesses assistance with OH&S and HR matters to ensure that their employees and the public are safe in the workplace and that they are meeting their legislative requirements. Would like to see the words 'practical workplace safety solutions' on the card. Personal details on the back. It needs to be clean, smart and professional (no fluff). Would like to see a simple logo if possible as well. Have been looking at orange and black, but open to other ideas.
Updates
Thank you to those to have created designs for us so far! We are really impressed with the impact of the black and orange having now seen it. Would be great if any further designs used those colours. Cheers.

Thank you to everyone that submitted a design. Your work is of the highest quality and we had a hard decision deciding. Sorry if we didn't choose your design, but it just came down to the one that stood out to us personally. Cheers.

Target Market(s)
Small-Medium business owners in Queensland, Australia. Age 25-60 male and female. Initially targeting those in the trade type industries
Industry/Entity Type
Health
Look and feel
Each slider illustrates characteristics of the customer's brand and the style your logo design should communicate.

```html
<!DOCTYPE html>
<html lang="en">
<head>
<meta charset="utf-8">
<title>Worksure Path — Business Card</title>
<link rel="stylesheet" href="https://fonts.googleapis.com/css2?family=Oswald:wght@300;400&display=swap">
<style>
  :root {
    --page-bg: #e9e6e2;
    --card-bg: #f7f7f6;
    --brand-orange: #e8643a;
    --brand-dark: #5b4f4b;
    --tagline-grey: #7d7470;
    --rule-grey: #b9b6b3;
    --card-shadow: rgba(40, 30, 20, 0.22);
  }
  * { box-sizing: border-box; margin: 0; padding: 0; }
  html, body {
    width: 1200px;
    height: 900px;
    overflow: hidden;
    background: var(--page-bg);
    font-family: "Oswald", "Arial Narrow", sans-serif;
  }
  .canvas {
    width: 1200px;
    height: 900px;
    display: flex;
    flex-direction: column;
    align-items: center;
    justify-content: center;
    gap: 56px;
  }
  .card {
    position: relative;
    width: 600px;
    height: 366px;
    background: var(--card-bg);
    box-shadow: 0 10px 28px var(--card-shadow);
  }

  /* Back: personal details */
  .card-back .rule {
    position: absolute;
    background: var(--rule-grey);
  }
  .card-back .rule-top { left: 0; right: 0; top: 112px; height: 1px; }
  .card-back .rule-bottom { left: 0; right: 0; top: 212px; height: 1px; }
  .card-back .rule-divider { left: 300px; top: 112px; width: 1px; height: 100px; }
  .holder-name {
    position: absolute;
    left: 36px;
    top: 148px;
    width: 250px;
    font-weight: 300;
    font-size: 27px;
    letter-spacing: 0.5px;
    color: var(--brand-orange);
    text-transform: uppercase;
  }
  .contact {
    position: absolute;
    left: 322px;
    top: 124px;
    color: var(--brand-orange);
    font-weight: 300;
    text-transform: uppercase;
  }
  .contact-phone { font-size: 21px; letter-spacing: 1.5px; display: block; }
  .contact-email { font-size: 13px; letter-spacing: 1.5px; display: block; margin-top: 10px; }
  .website {
    position: absolute;
    left: 322px;
    top: 238px;
    font-size: 13px;
    letter-spacing: 2px;
    font-weight: 300;
    color: var(--brand-orange);
    text-transform: uppercase;
  }

  /* Front: brand */
  .card-front .brand {
    position: absolute;
    left: 0; right: 0;
    top: 128px;
    display: flex;
    align-items: center;
    justify-content: center;
    gap: 20px;
  }
  .brand-square {
    width: 86px;
    height: 86px;
    background: var(--brand-orange);
    flex: none;
  }
  .brand-text { display: flex; flex-direction: column; }
  .brand-name {
    font-weight: 300;
    font-size: 56px;
    line-height: 1;
    letter-spacing: -1px;
    color: var(--brand-dark);
    text-transform: uppercase;
  }
  .brand-tagline {
    margin-top: 6px;
    font-weight: 400;
    font-size: 13px;
    letter-spacing: 2.4px;
    color: var(--tagline-grey);
    text-transform: uppercase;
  }
</style>
</head>
<body>
<main class="canvas">
  <section class="card card-back" aria-label="Card back with personal details">
    <span class="rule rule-top"></span>
    <span class="rule rule-bottom"></span>
    <span class="rule rule-divider"></span>
    <h1 class="holder-name">Daniel Corrigan</h1>
    <p class="contact">
      <span class="contact-phone">0491 562 338</span>
      <span class="contact-email">daniel@worksurepath.net.au</span>
    </p>
    <p class="website">www.worksurepath.net.au</p>
  </section>

  <section class="card card-front" aria-label="Card front with brand">
    <div class="brand">
      <span class="brand-square" aria-hidden="true"></span>
      <div class="brand-text">
        <h2 class="brand-name">Worksure Path</h2>
        <p class="brand-tagline">Practical workplace safety solutions</p>
      </div>
    </div>
  </section>
</main>
</body>
</html>
```